Updated brief for New ecommerce site needs a stunning business card that links to web site.

Updated business card brief. Please refer to the new files uploaded today (the last two) which show the background colour/style that we will be using in our web template for on-line trading, the grey marble concrete look.

Please see if you can use the grey marble background in the business card design in a way so it relates to our web template. It also needs to be transferable to banner ad, chatterbay ad etc.
brivo hub is a NEW eCommerce website which is commencing selling via tradlo & sellnook, used & damaged mobile phones & accessories, evolving into a full eCommerce store.

We like strong clean lines, use of a circle, in essence this will become our logo as well. Colours strong orange/Black/White The orange stronger than in CraftPanel #5352704 & grey marble as per file attached #153082

We love the use of a circle!! As we are evolving & moving forward this is what the circle represents to us……. ongoing change.

Front side with a circle with brivo hub in a modern font in the middle, brivo is in a strong orange and group is in black or white. On the reverse side, use layout as per Lumerax design from pelk.example. for icon details (not the boarder at top/botto).

This design is to meet www.pelk.example luxe cards specifications
Thank you we look forward to last minute inspiration.
Updates

Target Market(s)

Suppliers & business networking

Industry/Entity Type

Business

Contact Information for Business Card

Sam Ruiz
Director
mob +61 4987 6543
Locked Bag WXYZ 5678 QRS
sam@brivohub.example.au
www.brivohub.example.au

Requirements
Must have
• Design to meet www.pelk.example luxe business card specifications
• Colours - orange needs to be bold and strong & /black/white
• Circle with brivo hub in the middle
Nice to have
• Grey marble background incorporated into design in someway so it links with our web page.

```html
<!DOCTYPE html>
<html lang="en">
<head>
<meta charset="utf-8">
<title>brivo hub – business card</title>
<link rel="stylesheet" href="https://fonts.googleapis.com/css2?family=Arimo:wght@400;700&display=swap">
<style>
  :root {
    --stage: #d6d6d6;
    --orange-deep: #e25e17;
    --orange-glow: #f09a0a;
    --orange-text: #e4661b;
    --card-black: #060807;
    --ink: #111111;
    --white: #ffffff;
    --rule: #8a8a8a;
  }
  * { margin: 0; padding: 0; box-sizing: border-box; }
  html, body { width: 1200px; height: 1000px; overflow: hidden; }
  body {
    position: relative;
    background: var(--stage);
    font-family: "Arimo", Arial, sans-serif;
  }
  .card {
    position: absolute;
    left: 352px;
    width: 505px;
    height: 327px;
  }
  .card-front {
    top: 146px;
    background: radial-gradient(circle at 50% 50%, var(--orange-glow) 0%, var(--orange-glow) 28%, var(--orange-deep) 62%, var(--orange-deep) 100%);
  }
  .logo-circle {
    position: absolute;
    left: 143px;
    top: 55px;
    width: 220px;
    height: 220px;
    border-radius: 50%;
    background: var(--white);
    display: flex;
    align-items: center;
    justify-content: center;
  }
  .logo-name {
    text-align: center;
    font-family: "Arimo", Arial, sans-serif;
    font-weight: 700;
    font-size: 38px;
    line-height: 1.05;
    color: var(--ink);
  }

  .card-back { top: 536px; background: var(--card-black); }
  .holder { position: absolute; left: 107px; top: 108px; }
  .holder-name { font-size: 26px; font-weight: 700; color: var(--orange-text); line-height: 1; }
  .holder-role { font-size: 19px; color: var(--white); margin-top: 6px; line-height: 1; }
  .divider {
    position: absolute;
    left: 36px;
    top: 177px;
    width: 434px;
    height: 2px;
    background: linear-gradient(90deg, transparent, var(--rule) 30%, #c8c8c8 50%, var(--rule) 70%, transparent);
  }
  .contacts { position: absolute; left: 76px; top: 190px; list-style: none; }
  .contacts li {
    display: flex;
    align-items: center;
    height: 27.5px;
    font-size: 19.5px;
    font-weight: 700;
    color: var(--white);
  }
  .contacts svg { width: 18px; height: 18px; margin-right: 14px; flex: none; }
</style>
</head>
<body>
  <section class="card card-front" aria-label="Card front">
    <div class="logo-circle">
      <p class="logo-name">brivo<br>hub</p>
    </div>
  </section>

  <section class="card card-back" aria-label="Card back">
    <div class="holder">
      <p class="holder-name">Sam Ruiz</p>
      <p class="holder-role">Director</p>
    </div>
    <div class="divider"></div>
    <ul class="contacts">
      <li>
        <svg viewBox="0 0 18 18" fill="none" stroke="#fff" stroke-width="1.5"><rect x="5" y="1" width="8" height="15" rx="1.5"/><circle cx="9" cy="13" r="0.8" fill="#fff"/></svg>
        +61 4987 6543
      </li>
      <li>
        <svg viewBox="0 0 18 18" fill="none" stroke="#fff" stroke-width="1.6"><path d="M9 1.5a5.5 5.5 0 0 1 3.5 9.8L7 16.5l.5-5.2A5.5 5.5 0 0 1 9 1.5z"/></svg>
        Locked Bag WXYZ 5678 QRS
      </li>
      <li>
        <svg viewBox="0 0 18 18" fill="none" stroke="#fff" stroke-width="1.4"><rect x="1.5" y="4" width="15" height="10"/><path d="M1.5 4l7.5 6 7.5-6"/></svg>
        sam@brivohub.example.au
      </li>
      <li>
        <svg viewBox="0 0 18 18" fill="none" stroke="#fff" stroke-width="1.2"><circle cx="9" cy="9" r="7"/><ellipse cx="9" cy="9" rx="3" ry="7"/><path d="M2 9h14M3 5.5h12M3 12.5h12"/></svg>
        www.brivohub.example.au
      </li>
    </ul>
  </section>
</body>
</html>
```